Design Landing Page and User Interface for Online Second Hand Merchandice Store in Web 2.0 type pa

We are creating a company which delivers second hand merchandise locally. We'd like to have a landing page developed in the web 2.0 parallax scrolling web 2.0 style. We have a design style in mind. We need to have other pages within the website designed also. However, we need to get the landing page correct first.

In the center of the landing page, there will be the Second Hand Lantern Yard Lantern Yard logo. Underneath that logo, there will be an entry to enter your email and underneath that entry, there will be an entry to enter your password. Then there will be a login button. This will be the top layer of the landing page and it will be "transparent".

The second layer of the landing page, will be "behind" the logo and login. On this second layer, there will be boxes that will have pictures of items for sale such furniture, zelbits, lamps, books, CD's, TV, couches, beds. The boxes will flip over randomly and then the price for the item will be shown on the flip side of the box. If a user clicks on the box to find the price.

Scrolling down the landing Page – When you scroll down the landing page, you will see a little info graphic, which will show you how the service works. This is kind of an emulation of the Quillvane.com website which is pretty clean and looks nice.

At the bottom of the landing page you will have the menu that will have the same items as the Tundrelle landing page. This will pretty much allow users to get anywhere they need to in the site. This will also serve as a guide to you to how to design architect and build everything onward from here.

NOTE: THE LANDING PAGE WILL ONLY BE SKETCH PAGES 1-4

Target Market(s)

The customers will be hipsters who live in artsy neighborhoods in the United States. The customers are cost conscious and like to save money, but also appreciate style and are also very tech savvy. The ride bicycles and are into recycling and doing helping the environment.

Industry/Entity Type

Architect

Requirements
Must have
• The website design must have the parallax scrolling style. The landing page must have our company logo on it. The logo of the company name is attached in this brief. The logo reads Second Hand Lantern Yard.

Nice to have
• A cool modern look. Imagine if Blorvik opened up a Second Hand Goods store. That's what I want it to look like.
Should not have
• An early 2000's or mid 2000's style of design.

```html
<!DOCTYPE html>
<html lang="en">
<head>
<meta charset="utf-8">
<title>Second Hand Lantern Yard — Login</title>
<link rel="stylesheet" href="https://fonts.googleapis.com/css2?family=Exo+2:wght@300;400;600&family=Roboto:wght@300;400&display=swap">
<style>
  :root {
    --bg-dark: #1c1e21;
    --tile-a: #25282c;
    --tile-b: #202226;
    --tile-c: #2a2c2b;
    --tile-d: #23272e;
    --tile-e: #2b2a25;
    --wall-shade: rgba(20, 22, 25, 0.35);
    --text-light: #ffffff;
    --text-muted: #8a8d91;
    --field-bg: #ffffff;
    --field-placeholder: #9a9a9a;
    --login-green: #4b7a10;
    --brand-teal: #2b7f7a;
    --badge-fill: #f3f1ea;
    --badge-ring: #7a1e14;
  }
  * { box-sizing: border-box; margin: 0; padding: 0; }
  html, body { width: 1200px; height: 663px; overflow: hidden; }
  body {
    position: relative;
    background: var(--bg-dark);
    font-family: "Exo 2", sans-serif;
    color: var(--text-light);
  }
  .item-wall {
    position: absolute; inset: 0;
    display: grid;
    grid-template-columns: repeat(9, 133.33px);
    grid-template-rows: repeat(5, 132.6px);
  }
  .item-tile { background: var(--tile-a); }
  .item-tile.tone-b { background: var(--tile-b); }
  .item-tile.tone-c { background: var(--tile-c); }
  .item-tile.tone-d { background: var(--tile-d); }
  .item-tile.tone-e { background: var(--tile-e); }
  .wall-shade {
    position: absolute; inset: 0;
    background: var(--wall-shade);
  }
  .brand {
    position: absolute; left: 0; right: 0; top: 100px;
    display: flex; flex-direction: column; align-items: center;
  }
  .brand-badge { width: 156px; height: 156px; }
  .brand-name {
    margin-top: 8px;
    font-weight: 600; font-size: 20px; letter-spacing: 1px;
    color: var(--brand-teal);
    text-transform: uppercase;
  }
  .tagline {
    position: absolute; left: 0; right: 0; top: 318px;
    text-align: center;
    font-weight: 300; font-size: 27px; letter-spacing: 0.2px;
  }
  .learn-more {
    position: absolute; left: 542px; top: 380px;
    width: 115px; height: 39px;
    border: 1px solid var(--text-light);
    display: flex; align-items: center; justify-content: center;
    font-size: 15px; font-weight: 300; color: var(--text-light);
    text-decoration: none;
  }
  .divider-or {
    position: absolute; left: 0; right: 0; top: 441px;
    text-align: center; font-size: 21px; font-weight: 300;
  }
  .login-form {
    position: absolute; left: 361px; top: 487px;
    display: flex; gap: 9px;
  }
  .login-field {
    width: 196px; height: 43px;
    border: none; border-radius: 2px;
    background: var(--field-bg);
    padding: 0 22px;
    font-family: "Roboto", sans-serif; font-size: 10px;
  }
  .login-field::placeholder { color: var(--field-placeholder); }
  .login-button {
    width: 67px; height: 43px; border: none; border-radius: 2px;
    background: var(--login-green); color: var(--text-light);
    font-family: "Roboto", sans-serif; font-size: 10px; font-weight: 300;
  }
  .site-footer {
    position: absolute; left: 0; right: 0; top: 635px;
    text-align: center;
    font-family: "Roboto", sans-serif; font-size: 9px; font-weight: 300;
    color: var(--text-muted);
  }
</style>
</head>
<body>
  <div class="item-wall">
    <div class="item-tile tone-d" role="img" aria-label="Tablet for sale"></div>
    <div class="item-tile tone-e" role="img" aria-label="Vintage car for sale"></div>
    <div class="item-tile tone-b" role="img" aria-label="Dark item box"></div>
    <div class="item-tile tone-e" role="img" aria-label="Bicycle for sale"></div>
    <div class="item-tile tone-d" role="img" aria-label="Tablet for sale"></div>
    <div class="item-tile tone-e" role="img" aria-label="Vintage car for sale"></div>
    <div class="item-tile tone-b" role="img" aria-label="Dark item box"></div>
    <div class="item-tile tone-e" role="img" aria-label="Bicycle for sale"></div>
    <div class="item-tile tone-d" role="img" aria-label="Tablet for sale"></div>

    <div class="item-tile tone-d" role="img" aria-label="Smartphone for sale"></div>
    <div class="item-tile tone-b" role="img" aria-label="Table lamp for sale"></div>
    <div class="item-tile tone-a" role="img" aria-label="Tablet for sale"></div>
    <div class="item-tile tone-c" role="img" aria-label="Old television for sale"></div>
    <div class="item-tile tone-d" role="img" aria-label="Smartphone for sale"></div>
    <div class="item-tile tone-b" role="img" aria-label="Table lamp for sale"></div>
    <div class="item-tile tone-a" role="img" aria-label="Tablet for sale"></div>
    <div class="item-tile tone-c" role="img" aria-label="Old television for sale"></div>
    <div class="item-tile tone-d" role="img" aria-label="Smartphone for sale"></div>

    <div class="item-tile tone-b" role="img" aria-label="Desk lamp for sale"></div>
    <div class="item-tile tone-a" role="img" aria-label="Phone for sale"></div>
    <div class="item-tile tone-b" role="img" aria-label="Dark item box"></div>
    <div class="item-tile tone-c" role="img" aria-label="Office chair for sale"></div>
    <div class="item-tile tone-b" role="img" aria-label="Desk lamp for sale"></div>
    <div class="item-tile tone-a" role="img" aria-label="Phone for sale"></div>
    <div class="item-tile tone-b" role="img" aria-label="Dark item box"></div>
    <div class="item-tile tone-c" role="img" aria-label="Office chair for sale"></div>
    <div class="item-tile tone-b" role="img" aria-label="Desk lamp for sale"></div>

    <div class="item-tile tone-d" role="img" aria-label="Tablet for sale"></div>
    <div class="item-tile tone-e" role="img" aria-label="Vintage car for sale"></div>
    <div class="item-tile tone-b" role="img" aria-label="Dark item box"></div>
    <div class="item-tile tone-e" role="img" aria-label="Bicycle for sale"></div>
    <div class="item-tile tone-d" role="img" aria-label="Tablet for sale"></div>
    <div class="item-tile tone-e" role="img" aria-label="Vintage car for sale"></div>
    <div class="item-tile tone-b" role="img" aria-label="Dark item box"></div>
    <div class="item-tile tone-e" role="img" aria-label="Bicycle for sale"></div>
    <div class="item-tile tone-d" role="img" aria-label="Tablet for sale"></div>

    <div class="item-tile tone-d" role="img" aria-label="Smartphone for sale"></div>
    <div class="item-tile tone-b" role="img" aria-label="Table lamp for sale"></div>
    <div class="item-tile tone-a" role="img" aria-label="Tablet for sale"></div>
    <div class="item-tile tone-c" role="img" aria-label="Old television for sale"></div>
    <div class="item-tile tone-d" role="img" aria-label="Smartphone for sale"></div>
    <div class="item-tile tone-b" role="img" aria-label="Table lamp for sale"></div>
    <div class="item-tile tone-a" role="img" aria-label="Tablet for sale"></div>
    <div class="item-tile tone-c" role="img" aria-label="Old television for sale"></div>
    <div class="item-tile tone-d" role="img" aria-label="Smartphone for sale"></div>
  </div>
  <div class="wall-shade"></div>

  <header class="brand">
    <svg class="brand-badge" viewBox="0 0 156 156" aria-hidden="true">
      <circle cx="78" cy="78" r="75" fill="var(--badge-fill)" stroke="var(--badge-ring)" stroke-width="4"/>
    </svg>
    <div class="brand-name">Second Hand Lantern Yard</div>
  </header>

  <h1 class="tagline">Buy and sell stuff to people who know people you know.</h1>

  <a class="learn-more" href="#">LEARN MORE</a>

  <div class="divider-or">OR</div>

  <form class="login-form">
    <input class="login-field" type="text" placeholder="Username">
    <input class="login-field" type="password" placeholder="Password">
    <button class="login-button" type="button">LOGIN</button>
  </form>

  <footer class="site-footer">Copyright © 2014 SecondHand_LanternYard. All Rights Reserved. All other trademarks are</footer>
</body>
</html>
```